Deckblatt für Word-Vorlagen für Sachverständigen und Gutachter für stationäre Gaswarnanlagen
Zielgruppe
Ich bin Sachverständiger und Gutachter für stationäre Gaswarnanlagen. Dies kann man sich vorstellen wie eine Brandmeldeanlage nur für Gase, also Bereich Mess- und Regeltechnik gemischt mit Sicherheitstechnik und dies rein als Sachverständiger.
Meine Zielgruppe sind rein nur Firmen und davon meistens Großkonzerne. Mein Erscheinungsbild muss als Wertig, Seriös und Teuer sein.
Aufgabenstellung
Ich benötige nur ein neues Deckblatt für Word-Vorlagen.
Das Deckblatt ist rein für meine Gutachten und Beurteilungen, sollte also nicht 'verspielt' sein.
Anbei die alte Version mit einer Office Vorlage und den Daten welche ich immer eintragen muss. Zusätzlich anbei meine neue Power Point Masterfolien-Vorlage, rein als Info. Das Deckblatt, wie auch alle späteren Seiten, sollen das Wasserzeichen (rundes Logo) behalten.

```html
<!DOCTYPE html>
<html lang="de">
<head>
<meta charset="utf-8">
<title>Auftragsgutachten – Deckblatt</title>
<link rel="stylesheet" href="https://fonts.googleapis.com/css2?family=Poppins:wght@400;600;700;800&display=swap">
<style>
  :root {
    --stage: #d4d4d4;
    --page-light: #eef6fa;
    --page-mid: #d6e8f1;
    --title-blue: #124c94;
    --brand-blue: #2a4f78;
    --cyan: #00cbfb;
    --navy: #173f5f;
    --text-dark: #333a40;
    --white: #ffffff;
  }
  * { margin: 0; padding: 0; box-sizing: border-box; }
  html, body { width: 1200px; height: 1200px; overflow: hidden; }
  body {
    background: var(--stage);
    font-family: "Poppins", sans-serif;
    position: relative;
  }
  .cover {
    position: absolute;
    left: 211px; top: 50px;
    width: 778px; height: 1100px;
    background:
      radial-gradient(circle at 53% 51%, rgba(255,255,255,0.9) 0%, rgba(255,255,255,0) 45%),
      linear-gradient(180deg, var(--page-mid) 0%, var(--page-light) 45%, var(--page-mid) 75%, var(--page-light) 100%);
    overflow: hidden;
  }
  .brand {
    position: absolute; top: 52px; left: 0; width: 100%;
    display: flex; justify-content: center; align-items: center; gap: 12px;
  }
  .brand-dot {
    width: 48px; height: 48px; border-radius: 50%;
    background: var(--brand-blue);
  }
  .brand-text { display: flex; flex-direction: column; }
  .brand-name {
    font-weight: 600; font-size: 27px; line-height: 1.05;
    color: var(--brand-blue);
  }
  .brand-tagline {
    font-size: 12px; letter-spacing: 1.3px; color: var(--text-dark);
  }
  .doc-title {
    position: absolute; top: 200px; left: 0; width: 100%;
    text-align: center; color: var(--title-blue);
    font-weight: 800; font-size: 74px; line-height: 74px; letter-spacing: 0.5px;
  }
  .doc-title span { display: block; margin-bottom: 0; }
  .seal {
    position: absolute; left: 290px; top: 393px;
    width: 196px; height: 196px; border-radius: 50%;
    background: radial-gradient(circle at 50% 40%, #ffffff 0%, #f2f4f6 60%, #d7dde2 100%);
    box-shadow: 0 4px 12px rgba(0,0,0,0.15);
  }
  .expert {
    position: absolute; top: 630px; left: 0; width: 100%;
    text-align: center;
  }
  .expert-name {
    font-weight: 700; font-size: 21px; color: var(--title-blue); line-height: 30px;
  }
  .expert-role {
    font-size: 19.5px; color: var(--text-dark); line-height: 30px;
  }
  .report-number {
    position: absolute; top: 799px; left: 0; width: 100%; height: 57px;
    background: var(--cyan); color: var(--white);
    font-weight: 700; font-size: 18px;
    display: flex; align-items: center; justify-content: center;
  }
  .info-box {
    position: absolute; top: 866px; height: 122px;
    background: var(--navy); color: var(--white);
    padding: 18px 0 0 79px;
  }
  .info-client { left: 0; width: 384px; }
  .info-site { left: 394px; width: 384px; padding-left: 50px; }
  .info-label {
    font-weight: 700; font-size: 17px; color: var(--cyan); line-height: 22px; margin-bottom: 3px;
  }
  .info-line { font-size: 15px; line-height: 22px; }
  .footer {
    position: absolute; top: 1030px; left: 0; width: 100%;
    text-align: center; font-size: 15px; color: #222;
  }
  .footer strong { color: var(--title-blue); font-weight: 700; }
</style>
</head>
<body>
  <main class="cover">
    <header class="brand">
      <div class="brand-dot"></div>
      <div class="brand-text">
        <div class="brand-name">Taloris Gasprüfung</div>
        <div class="brand-tagline">Beratung in Sachen Gaswarntechnik</div>
      </div>
    </header>

    <h1 class="doc-title"><span>AUFTRAGS</span><span>GUTACHTEN</span></h1>

    <div class="seal" role="img" aria-label="Prüfsiegel des Sachverständigenverbands"></div>

    <section class="expert">
      <div class="expert-name">KONRAD WEIDLICH</div>
      <div class="expert-role">Geprüfter Sachverständiger</div>
      <div class="expert-role">für Gaswarntechnik</div>
      <div class="expert-role">Fachkraft für Explosionsschutz</div>
    </section>

    <div class="report-number">Gutachten-Nr. 1202/001-01 vom 19. March 2024</div>

    <section class="info-box info-client">
      <div class="info-label">AUFTRAGGEBER</div>
      <div class="info-line">Agrarhandel Mittelrhein eG</div>
      <div class="info-line">Kastanienallee 4</div>
      <div class="info-line">D-50668 Köln</div>
    </section>

    <section class="info-box info-site">
      <div class="info-label">STANDORT</div>
      <div class="info-line">Pflanzenschutzmittellager</div>
      <div class="info-line">Lindenhofstraße 22</div>
      <div class="info-line">D-41460 Neuss</div>
    </section>

    <footer class="footer">
      Weidengasse 9 • 35510 Butzbach <strong>• 06004/55180-0 • info@taloris-gaspruefung.de</strong>
    </footer>
  </main>
</body>
</html>
```